依頼詳細
2種類のラベルデザインを募集します。

①ワイン名「Vou Vou」
当然日本語の色の意味もありますが、イタリア語で「Vou!」というと「さあ!」とか「ほら!」といった意味があります。カジュアルな表現で、仲間を鼓舞するために「さあ行こうぜ」といったニュアンスで「Vou Vou!」などと使ったりします。

②ワイン名「Velustra」
オレンジを意味するラテン語です。

・一般の最終消費者にアイキャッチなラベルデザインを希望します
・「自然派」というコンセプトにあったデザインを希望します
・オーガニック志向の消費者に対して訴求力のあるラベルデザインを希望します
・前述の通りこのワインにフルーツのオレンジは関連性がないので、誤解を避けるためフルーツのオレンジのイラストはNGでお願いします

記載項目
ラベルサイズは縦が95mm以下。横は80mm以下。
ラベルには下記の情報を入れ込んで作成をお願いします。
・ワイン名
・ヴィンテージである「2021」
・容量である「750ml」
・イタリア産を意味する「Prodotto in Italia」の表記
・ノンフィルターを意味する「Non Filtered」の表記
書式は自由です。大文字・小文字なども自由です。
希望イメージ
シンプル 複雑
単色 カラフル
暗い 明るい
日常 高級
遊び心 厳粛
未来的 伝統的
女性的 男性的
希望する色
黄・オレンジ系
納品ファイル
• 高解像度JPG (.jpg)
• イラストレーター形式 (.ai)
補足説明
ご質問をいただきましたので、ボトル形状とビンの色予定を追記します。

ボトルは透明瓶、形状はブルゴーニュ形の予定です。
写真も添付致しました。

どうぞ宜しくお願い位致します。
いくつもラベルデザインご提案を頂き、誠にありがとうございます。
ただ、もう少し選択肢を増やした中からデザインを選び決めたいと考え、提案締め切り日を延長させていただくこととしました。

引き続きどうぞ宜しくお願い致します。
■ 選んだ理由

2種類のワインそれぞれを提案するお客様企業様の志向も含めデザインを選定させていただくこととなりました。
商品のターゲティング上、一般最終消費者のお客様が手に取りやすく、記憶に残りやすいラベルであることが1番の決め手となりました。

■ 提案者全員のお礼・コメント

大変たくさんのご提案を頂戴し、誠にありがとうございます。
採用できなかった他のラベルも非常に素敵なものばかりで、不採用とするのがもったいないものばかりです。

弊社としては今回初めてコンペをさせていただきましたが、期待以上にレベルの高いご提案をいくつもいただくことができることがわかりました。これをひとつのロールモデルとして、今後もごコンペの募集をさせていただくかもしれません。その時は変わらずのお引き立てをお願い致します。

ありがとうございました。

```html
<!DOCTYPE html>
<html lang="en">
<head>
<meta charset="UTF-8">
<title>Vou Vou — Wine Label</title>
<link rel="stylesheet" href="https://fonts.googleapis.com/css2?family=Montserrat:wght@400;500&display=swap">
<style>
  :root {
    --paper: #ffffff;
    --amber: #d99a52;
    --ink: #2a2622;
    --ink-soft: #6d655d;
  }
  html, body {
    margin: 0;
    padding: 0;
    width: 855px;
    height: 1200px;
    overflow: hidden;
    background: var(--paper);
  }
  .label {
    position: relative;
    width: 855px;
    height: 1200px;
    background: var(--paper);
    overflow: hidden;
  }
  .brand {
    position: absolute;
    left: 0;
    right: 0;
    top: 430px;
    display: flex;
    align-items: center;
    justify-content: center;
    gap: 32px;
  }
  .brand-dot {
    width: 84px;
    height: 84px;
    border-radius: 50%;
    background: var(--amber);
    flex: none;
  }
  .wine-name {
    margin: 0;
    font-family: "Montserrat", sans-serif;
    font-weight: 500;
    font-size: 96px;
    line-height: 1;
    letter-spacing: 2px;
    color: var(--ink);
    white-space: nowrap;
  }
  .vine-sprig {
    position: absolute;
    left: 362px;
    top: 620px;
    width: 130px;
    height: 120px;
    border-radius: 50%;
    background: radial-gradient(circle, rgba(217,154,82,0.28), rgba(217,154,82,0) 70%);
  }
  .vintage {
    position: absolute;
    left: 0;
    right: 0;
    top: 830px;
    margin: 0;
    text-align: center;
    font-family: "Montserrat", sans-serif;
    font-weight: 500;
    font-size: 34px;
    letter-spacing: 4px;
    color: var(--ink);
  }
  .details {
    position: absolute;
    left: 0;
    right: 0;
    top: 900px;
    margin: 0;
    display: flex;
    justify-content: center;
    gap: 38px;
    font-family: "Montserrat", sans-serif;
    font-weight: 400;
    font-size: 20px;
    letter-spacing: 1.5px;
    color: var(--ink-soft);
  }
</style>
</head>
<body>
  <main class="label">
    <div class="brand">
      <span class="brand-dot" aria-hidden="true"></span>
      <h1 class="wine-name">Vou Vou</h1>
    </div>
    <div class="vine-sprig" role="img" aria-label="Fine line drawing of a vine sprig with leaves and berries"></div>
    <p class="vintage">2021</p>
    <p class="details">
      <span>750ml</span>
      <span>Prodotto in Italia</span>
      <span>Non Filtered</span>
    </p>
  </main>
</body>
</html>
```